Business card design for new brand

We have recently rebranded and need a new business card template.

We are an insurance underwriting agency. All of our products are sold via other partner companies, so these are just to pass on our details to other organisations.

We would like to see designs that use the colour green (current stationary generally uses lime green (rgb 142,190,63) and forest green (0,154,79) to comply with our logo's colours. We are happy with other shades of green.

Business cards need to include our logo, as well as space for:
1. Full name
2. Qualifications (optional)
3. Title
4. Office number
5. Mobile number
6. Email address

Our logo is enclosed here.

```html
<!DOCTYPE html>
<html lang="en">
<head>
<meta charset="utf-8">
<title>Greenvale Cover – Business Card</title>
<link href="https://fonts.googleapis.com/css2?family=Montserrat:wght@500;600&family=Oswald:wght@500&display=swap" rel="stylesheet">
<style>
  :root {
    --backdrop: #2a2a2a;
    --card: #232323;
    --white: #ffffff;
    --ink: #111111;
    --lime: #8ebe3f;
    --forest: #009a4f;
  }
  * { box-sizing: border-box; margin: 0; padding: 0; }
  html, body { width: 1200px; height: 874px; overflow: hidden; }
  body {
    background: var(--backdrop);
    font-family: "Montserrat", Arial, sans-serif;
    position: relative;
  }
  .card {
    position: absolute;
    left: 302px;
    width: 596px;
    height: 340px;
    background: var(--card);
    border-radius: 4px;
    overflow: hidden;
  }
  .card--front { top: 60px; }
  .card--back { top: 474px; }

  .wordmark {
    display: flex;
    align-items: center;
    gap: 14px;
    font-weight: 600;
    line-height: 1.05;
  }
  .wordmark__square {
    width: 44px;
    height: 44px;
    background: var(--forest);
    flex: none;
  }
  .wordmark__name { font-size: 42px; }
  .wordmark__sub { font-size: 20px; padding-left: 2px; }

  .card--front .wordmark {
    position: absolute;
    left: 50%;
    top: 50%;
    transform: translate(-50%, -50%);
    color: var(--white);
  }

  .brand-panel {
    position: absolute;
    left: 282px;
    top: 56px;
    width: 314px;
    height: 240px;
    background: var(--white);
    display: flex;
    align-items: center;
    justify-content: center;
  }
  .brand-panel .wordmark { color: var(--ink); }
  .brand-panel .wordmark__name { font-size: 34px; }
  .brand-panel .wordmark__sub { font-size: 16px; }
  .brand-panel .wordmark__square { width: 34px; height: 34px; }

  .person {
    position: absolute;
    left: 40px;
    top: 150px;
  }
  .person__name {
    font-family: "Oswald", "Arial Narrow", sans-serif;
    font-weight: 500;
    font-size: 26px;
    letter-spacing: 0.5px;
    color: var(--forest);
    text-transform: uppercase;
    line-height: 1.1;
  }
  .person__title {
    font-size: 13px;
    font-weight: 600;
    color: var(--lime);
    margin-bottom: 16px;
  }
  .contact {
    display: flex;
    gap: 10px;
    margin-bottom: 12px;
    color: var(--white);
    font-size: 13px;
    font-weight: 600;
    line-height: 1.45;
  }
  .contact__icon { width: 22px; height: 22px; flex: none; margin-top: 1px; }
</style>
</head>
<body>

<section class="card card--front" aria-label="Card front">
  <div class="wordmark">
    <span class="wordmark__square"></span>
    <div>
      <div class="wordmark__name">Greenvale Cover</div>
      <div class="wordmark__sub">Australia Pty Ltd</div>
    </div>
  </div>
</section>

<section class="card card--back" aria-label="Card back">
  <div class="person">
    <div class="person__name">Daniel Hart</div>
    <div class="person__title">President</div>

    <div class="contact">
      <svg class="contact__icon" viewBox="0 0 22 22" aria-hidden="true">
        <polygon points="11,1 20,6 20,16 11,21 2,16 2,6" fill="var(--forest)"/>
        <path d="M8 6.5c.6 0 1.2 1.6 1.2 2.2 0 .5-.8.8-.8 1.2.3 1 1.7 2.4 2.7 2.7.4 0 .7-.8 1.2-.8.6 0 2.2.6 2.2 1.2 0 .8-.9 1.8-1.8 1.8-2.6-.2-6.4-4-6.6-6.6 0-.9 1-1.7 1.9-1.7z" fill="var(--lime)"/>
      </svg>
      <div>555-210-4471<br>555-318-2096</div>
    </div>

    <div class="contact">
      <svg class="contact__icon" viewBox="0 0 22 22" aria-hidden="true">
        <polygon points="11,1 20,6 20,16 11,21 2,16 2,6" fill="var(--forest)"/>
        <rect x="6" y="7.5" width="10" height="7" fill="var(--lime)"/>
        <path d="M6 7.5l5 4 5-4" fill="none" stroke="var(--forest)" stroke-width="1"/>
      </svg>
      <div>hello@greenvalecover.com<br>www.greenvalecover.com</div>
    </div>
  </div>

  <div class="brand-panel">
    <div class="wordmark">
      <span class="wordmark__square"></span>
      <div>
        <div class="wordmark__name">Greenvale Cover</div>
        <div class="wordmark__sub">Australia Pty Ltd</div>
      </div>
    </div>
  </div>
</section>

</body>
</html>
```